Maltese Sunscreen

I need 2 labels for 2 sunscreens.
1: 50SPF Sunscreen suitable for oily and acne prone skin ( elexir from maltese plants that help with excess oil)
2: 50SPF Sunscreen suitable for normal skin made out of essential oils that help to calm down nervous system and stimulate sensation of relaxation.

Not sure if its too much writing on the label ?

Attached is the logo and picture of the bottle, beige tannish color 50ml

I wanted to include : Product of Malta on the label with maltese flag ( i guess smaller than the rest of the text)
I can only use " suitable" and "helps" as it is cosmetic and not medical.

Target Market(s)

Men and women

Industry/Entity Type

Skin care

Requirements
Must have
• Logo, descripción, Maltese flag “ product of Malta. Incorporate Maltese landscape like in the picture, use Maltese clover flower like in picture attached.
Nice to have
• I want the label to be very Maltese. Depict the landscape of the picture attached, use clover flower, use the Maltese lady logo

```html
<!DOCTYPE html>
<html lang="en">
<head>
<meta charset="utf-8">
<title>Isolana Mineral Sunscreen Labels</title>
<link href="https://fonts.googleapis.com/css2?family=Montserrat:wght@400;500;600&display=swap" rel="stylesheet">
<style>
  :root {
    --page: #ffffff;
    --cream: #efe6dd;
    --tan: #ddb69b;
    --peach: #e2bda4;
    --ink: #4a4546;
    --soft-ink: #5a5253;
    --light: #f3e6da;
    --flag-white: #f1e3d6;
    --flag-red: #e56b68;
    --band-sand: #d9b59b;
    --band-stone: #bfb3b7;
    --band-rust: #b98c77;
  }
  * { margin: 0; padding: 0; box-sizing: border-box; }
  html, body {
    width: 1200px; height: 750px; overflow: hidden;
    background: var(--page);
    font-family: "Montserrat", sans-serif;
  }
  .stage { position: relative; width: 1200px; height: 750px; }
  .label {
    position: absolute; top: 93px; width: 268px; height: 490px;
    border-radius: 6px; text-align: center; color: var(--ink);
  }
  .label--oily { left: 290px; background: var(--cream); }
  .label--normal { left: 626px; background: var(--tan); }

  .brand { position: absolute; top: 48px; left: 0; right: 0; }
  .brand-mark {
    width: 74px; height: 74px; border-radius: 50%; margin: 0 auto 6px;
    background: var(--band-sand); opacity: .45;
  }
  .brand-name { font-size: 20px; font-weight: 500; letter-spacing: 1px; color: var(--ink); }
  .brand-tag { font-size: 5px; font-weight: 500; letter-spacing: .3px; color: var(--ink); margin-top: 2px; }

  .product-type { position: absolute; top: 156px; left: 0; right: 0; }
  .product-type .mineral { font-size: 19px; font-weight: 500; letter-spacing: 6px; color: var(--peach); padding-left: 6px; }
  .label--normal .product-type .mineral { color: var(--light); }
  .product-type .sunscreen { font-size: 9.5px; font-weight: 600; letter-spacing: 3px; color: var(--ink); margin-top: 1px; padding-left: 3px; }

  .landscape-band {
    position: absolute; top: 214px; left: 20px; right: 20px; height: 100px;
    background: linear-gradient(90deg, var(--band-sand), var(--band-rust) 30%, var(--light) 50%, var(--band-stone) 75%, var(--band-sand));
    opacity: .75; border-radius: 4px;
  }
  .spf-badge {
    position: absolute; top: 216px; left: 84px; width: 100px; height: 100px; border-radius: 50%;
    display: flex; flex-direction: column; align-items: center; justify-content: center;
  }
  .label--oily .spf-badge { background: var(--cream); }
  .label--normal .spf-badge { background: var(--tan); }
  .spf-number { font-size: 50px; font-weight: 500; line-height: 1; color: var(--peach); }
  .label--normal .spf-number { color: var(--light); }
  .spf-text { font-size: 15px; font-weight: 500; line-height: 1; color: var(--ink); }
  .label--normal .spf-text { color: var(--light); }

  .description {
    position: absolute; top: 338px; left: 18px; right: 18px;
    font-size: 7px; font-weight: 600; letter-spacing: .9px; line-height: 1.35; color: var(--ink);
  }
  .label--normal .description { top: 333px; line-height: 1.1; }
  .description .accent { color: var(--peach); }
  .label--normal .description .accent { color: var(--light); font-weight: 400; }
  .spectrum {
    position: absolute; top: 370px; left: 0; right: 0;
    font-size: 7px; font-weight: 600; letter-spacing: .9px; color: var(--ink);
  }
  .origin { position: absolute; top: 388px; left: 0; right: 0; }
  .origin svg { display: block; margin: 0 auto; }
  .origin-text {
    font-size: 6px; font-weight: 500; letter-spacing: .6px; line-height: 1; color: var(--soft-ink); margin-top: 3px;
  }
  .net {
    position: absolute; top: 446px; left: 0; right: 0;
    font-size: 7px; font-weight: 600; letter-spacing: .8px; color: var(--soft-ink);
  }
</style>
</head>
<body>
<main class="stage">

  <section class="label label--oily">
    <div class="brand">
      <div class="brand-mark" role="img" aria-label="Maltese landscape motif behind the brand name"></div>
      <div class="brand-name">Isolana</div>
      <div class="brand-tag">NATURAL SKIN COSMETICS</div>
    </div>
    <div class="product-type">
      <div class="mineral">MINERAL</div>
      <div class="sunscreen">SUNSCREEN</div>
    </div>
    <div class="landscape-band" role="img" aria-label="Maltese limestone coastline landscape in sand, rust and stone tones"></div>
    <div class="spf-badge">
      <span class="spf-number">50</span>
      <span class="spf-text">SPF</span>
    </div>
    <p class="description">ELEXIR FROM MALTESE PLANTS<br>THAT <span class="accent">HELP WITH EXCESS OIL</span></p>
    <p class="spectrum">BROAD SPECTRUM SPF 50</p>
    <div class="origin">
      <svg width="30" height="30" viewBox="0 0 30 30" aria-label="Flag of Malta">
        <rect x="0" y="0" width="30" height="30" rx="4" fill="var(--flag-white)"/>
        <path d="M15 0 H26 A4 4 0 0 1 30 4 V26 A4 4 0 0 1 26 30 H15 Z" fill="var(--flag-red)"/>
        <path d="M7 3.5 V9.5 M4 6.5 H10" stroke="var(--flag-red)" stroke-width="1.4"/>
      </svg>
      <div class="origin-text">PRODUCT<br>OF MALTA</div>
    </div>
    <p class="net">NET: 50ML</p>
  </section>

  <section class="label label--normal">
    <div class="brand">
      <div class="brand-mark" role="img" aria-label="Maltese landscape motif behind the brand name"></div>
      <div class="brand-name">Isolana</div>
      <div class="brand-tag">NATURAL SKIN COSMETICS</div>
    </div>
    <div class="product-type">
      <div class="mineral">MINERAL</div>
      <div class="sunscreen">SUNSCREEN</div>
    </div>
    <div class="landscape-band" role="img" aria-label="Maltese limestone coastline landscape in sand, rust and stone tones"></div>
    <div class="spf-badge">
      <span class="spf-number">50</span>
      <span class="spf-text">SPF</span>
    </div>
    <p class="description">SUNSCREEN SUITABLE FOR NORMAL<br>SKIN MADE <span class="accent">TO CALM DOWN NERVOUS<br>SYSTEM AND STIMULATE SENSATION<br>OF RELAXATION.S OIL</span></p>
    <p class="spectrum">BROAD SPECTRUM SPF 50</p>
    <div class="origin">
      <svg width="30" height="30" viewBox="0 0 30 30" aria-label="Flag of Malta">
        <rect x="0" y="0" width="30" height="30" rx="4" fill="var(--flag-white)"/>
        <path d="M15 0 H26 A4 4 0 0 1 30 4 V26 A4 4 0 0 1 26 30 H15 Z" fill="var(--flag-red)"/>
        <path d="M7 3.5 V9.5 M4 6.5 H10" stroke="var(--flag-red)" stroke-width="1.4"/>
      </svg>
      <div class="origin-text">PRODUCT<br>OF MALTA</div>
    </div>
    <p class="net">NET: 50ML</p>
  </section>

</main>
</body>
</html>
```